illustration of retro stamps to create a 'product label' for my services

I would like some retro looking 'lables' made for my services. I work in marketing and have a number of packages I often clients which I have given creative names to. The 4 packages & descriptions are below.

- spark the compass!
- Lift the tide!
- Harbour pilot crew
- Idea rally sessions

Spark the compass!
In this 3 hour ‘Spark the compass’ work shop we’ll strategise what your brand stands for, how it is perceived by clients and how it needs to be communicated to ensure that your business can grow in a competitive market. Don’t forget, perception is reality so the right brand image gets you off the ground faster. Let’s make sure that your brand is evoking the right reaction and opinions from your target market. After all, the right image builds brand equity which builds reputation.
 Spark the compass workshop includes”
 A clear brand message to communicate who you are and what you offer the market
 Free list of tips on how to generate more customers without spending any marketing dollars
 A fresh objective perspective on what changes can be made to your marketing collateral to give you the biggest bang for your buck
 A thorough strategic analysis on your products/services and how you can get customers to literally forget the competition when considering your brand
 Sales tips on how to effectively engage with clients about your brand
$395-

Lift the tide!
If you’d like to take your biz and level of planning to the next level and get your business thrust further into the spot light then the ‘Lift the tide’ package is the one for you..
Your target market need to know how your brand and business can help them and any business that wants to be successful knows that communication and a focused marketing strategy are integral to growth
The ‘lift the tide’ package is a 4 hour workshop, where we get straight down to business to boost your business! Collectively, we’ll devise a strategic 12 month marketing plan with internal and external marketing activities and communications to ensure that you are consistently generating new sales leads to the business.
We’ll spend 1 hour of the workshop to give you a slice of the ‘deal ladder method’ to ensure that front end client discussions with prospects are maximised fully so that your sales are winning!
What you walk away with:
 A clear understanding of your business, the market and competitors and a new list of opportunities ready for your business to go forward
 A comprehensive 12 month marketing plan for your business on how you can get noticed, sell your products and services and boost your revenue
 New opportunity areas that you may not have already considered
 A review of marketing collateral including website and how more leads can be generated to the business
 A Free list of ways to get noticed in the media and get your brand optimal exposure
 An snapshot overview of the ‘Deal Ladder Method’ so you can get out there and apply an easily replicable model for confidently engaging and communicating with clients and get your brand sold
 A FREE list of social media tips to make communications relevant to your audience
 A developed list of potential strategic partners to move forward with

$695-

Of course, if you decide that you don’t have the time to implement the marketing plan, then we- as your harbour pilot Crew- can do that for you. Check out our weekly retainer

Harbour Pilot Crew!
Designed for the humble small business who wants all the bells and whistles, but perhaps are not able to hire a full time professional. We offer your business a dedicated marketing consultant who will execute a range of exciting initiatives from your marketing plan as well as the following... all designed to help your business flourish and be noticed!
 Execution of the agreed marketing plan
 Social media communications via chatterbox, work loop and peeper (2 x week) aimed at directing traffic back to blogs on your website
 Complete website management*
 Weekly business article written by our copywriting professionals to your database of customers via e-marketing
 Creation and management of competitions
 Weekly ‘profit kindler’ tips sent out to all internal staff includes loads of deal ladder tips to get customers converted
 1 x monthly writing services- i.e. newsletters, editorials, customer fact sheets, presentations (1 hour)
 1’where it’s at’ 30 minute phone conversation per week/ 1 45 minute face to face ‘debrief and strategise’ visit per month helps keep you accountable to business growth via your own dedicated marketing and sales strategist
 Bi Monthly Publicity and media relations media support via a dedicated & CMSN certified Public relations manager to ensure your brand is being seen in targeted publications
 1 x 3 hour ‘personality buying styles’ workshop whereby staff will learn the various personality types and how to learn the art of reading the client and their buying styles.
 1 x 3 hour deal ladder training to help you further explore the art of winning your clients
 1 x phone call per month to strategic partnership prospects to see how we can better leverage the business
 Graphic design inclusion for marketing collateral (1 campaign per quarter, printing costs excluded)
Extra value
 Upon commencement of our weekly marketing consultant retainer, we want to ensure that your website, marketing collateral and front end (team) are shining starts and all working to maximise your brand and dollars, so we’ll do the following:
 1 x free ‘name and email’ client ‘opt in’ to make sure you are continually growing your client list via your website
 1 x free email web check ensuring that the website is communicating your brand message clearly
 4 x 1 hour one on one sales coaching session to help you plan the best strategy when meeting with that awesome game changer prospect client.
 12 months worth of awesome motivation and an advocate for your business!

**Website management includes amendments, new pages, modifications, copy writing for the website, blog management. Excludes SEO.

Weekly retainer from $500 (based on a 12 month contract)

Idea Rally Sessions

Need someone to just ‘slam it out with’, your brand is going places and fast. You want a marketing and sales professional to guide you on where to go next, to offer objective advice, strategies and tips on ‘where to next’, help with motivating staff (or even yourself), marketing, branding, strategy or sales.

Idea rally sessions can be run on your agenda; weekly, fortnightly or monthly. We recommend one hour sessions face to face where we can ‘idea rally’ and get your brand solidified, your motivation boosted and your sales soaring.

$120 per hour

25-40 years start ups and small businesses, middle to high income earners, innovators.

Product

• The retro looking stamps must be contemporary and have a fresh modern feel. Please do not include any prices on the stamps, just simply the description of the product. Please see BOTH of the attached files for inspiration. I would like each label/illustration to have a different colour please.
• These will end up on my services page on my website www.quillharbor.com.au so please ensure that they have the appropriate function for this.

```html
<!DOCTYPE html>
<html lang="en">
<head>
<meta charset="utf-8">
<title>Idea Rally Sessions</title>
<link href="https://fonts.googleapis.com/css2?family=Arvo:wght@700&family=Carlito:ital,wght@0,700;1,700&display=swap" rel="stylesheet">
<style>
  :root {
    --page: #ffffff;
    --burst: #e6e6e6;
    --ring: #9a9a9a;
    --seal: #000000;
    --title: #444444;
    --star: #333333;
    --ribbon: #4cbb2a;
    --light: #ffffff;
  }
  html, body {
    margin: 0;
    padding: 0;
    overflow: hidden;
    background: var(--page);
  }
  .canvas {
    position: relative;
    width: 1200px;
    height: 848px;
    overflow: hidden;
    background: var(--page);
  }
  .badge {
    position: absolute;
    left: 0;
    top: 0;
  }
  .badge-title {
    font-family: "Arvo", Georgia, serif;
    font-weight: 700;
    font-size: 35px;
    fill: var(--title);
  }
  .price {
    font-family: "Carlito", "Calibri", Arial, sans-serif;
    font-weight: 700;
    font-size: 43px;
    fill: var(--light);
  }
  .description {
    position: absolute;
    left: 370px;
    top: 243px;
    width: 460px;
    margin: 0;
    text-align: center;
    color: var(--light);
    font-family: "Carlito", "Calibri", Arial, sans-serif;
    font-weight: 700;
    font-style: italic;
    font-size: 17.5px;
    line-height: 22px;
  }
  .description p {
    margin: 0;
  }
  .description p + p {
    margin-top: 22px;
  }
</style>
</head>
<body>
<main class="canvas">
  <svg class="badge" width="1200" height="848" viewBox="0 0 1200 848" xmlns="http://www.w3.org/2000/svg">
    <defs>
      <path id="title-arc" d="M 378 420 A 222 222 0 0 1 822 420"/>
      <polygon id="star" points="0,-12 2.8,-3.9 11.4,-3.7 4.5,1.5 7.1,9.7 0,4.8 -7.1,9.7 -4.5,1.5 -11.4,-3.7 -2.8,-3.9"/>
    </defs>

    <g class="starburst" fill="var(--burst)" transform="translate(600 420)">
      <rect x="-206.5" y="-206.5" width="413" height="413" transform="rotate(0)"/>
      <rect x="-206.5" y="-206.5" width="413" height="413" transform="rotate(11.25)"/>
      <rect x="-206.5" y="-206.5" width="413" height="413" transform="rotate(22.5)"/>
      <rect x="-206.5" y="-206.5" width="413" height="413" transform="rotate(33.75)"/>
      <rect x="-206.5" y="-206.5" width="413" height="413" transform="rotate(45)"/>
      <rect x="-206.5" y="-206.5" width="413" height="413" transform="rotate(56.25)"/>
      <rect x="-206.5" y="-206.5" width="413" height="413" transform="rotate(67.5)"/>
      <rect x="-206.5" y="-206.5" width="413" height="413" transform="rotate(78.75)"/>
    </g>

    <circle class="outer-disc" cx="600" cy="420" r="258" fill="var(--page)" stroke="var(--ring)" stroke-width="1.5"/>

    <path class="side-rule" d="M375.5,322 A245 245 0 0 0 402.5,565" fill="none" stroke="var(--ring)" stroke-width="6"/>
    <path class="side-rule" d="M824.5,322 A245 245 0 0 1 797.5,565" fill="none" stroke="var(--ring)" stroke-width="6"/>

    <circle class="seal" cx="600" cy="420" r="211" fill="var(--seal)"/>

    <text class="badge-title">
      <textPath href="#title-arc" startOffset="50%" text-anchor="middle">Idea Rally Sessions</textPath>
    </text>

    <use href="#star" x="401" y="297" fill="var(--star)"/>
    <use href="#star" x="795" y="297" fill="var(--star)"/>

    <polygon class="ribbon" points="358,585 842,585 822,617 842,649 358,649 378,617" fill="var(--ribbon)"/>
    <use href="#star" x="430" y="618" fill="var(--light)"/>
    <use href="#star" x="768" y="618" fill="var(--light)"/>
    <text class="price" x="601" y="631" text-anchor="middle">$120 per hour</text>
  </svg>

  <div class="description">
    <p>Need someone to just<br>'slam it out with', your brand<br>is going places and fast. You want<br>a marketing and sales professional to guide<br>you on where to go next, to offer objective advice,<br>strategies and tips on 'where to next', help with<br>motivating staff (or even yourself), marketing,<br>branding, strategy or sales.</p>
    <p>Idea rally sessions can be run on your agenda;<br>weekly, fortnightly or monthly. We recommend one<br>hour sessions face to face where we can<br>'idea rally' and get your brand solidified,<br>your motivation boosted and<br>your sales soaring.</p>
  </div>
</main>
</body>
</html>
```